Importance of fire extinguisher 2 sided postcard handout

I need somebody to design an eye catching handout the size of a postcard and double sided discussing the importance of fire extinguishers. I ca provide data on how vital they are how the save lives and how a fire extinguisher is used every 10 seconds. The card should state basics and urge the reader to understand the importance of fire extinguisher in a home. Contains a small lose to a full blown fire and should also emphasize that our product is an environmentally friendly product unlike other traditional fire extinguishers. It's safe to be used - is not toxic which is unique. Pictures of our unique product are included and information on fire extinguishers is also present for background info. I think our design should incorporate green since that is what makes this product unique. Final design should communicate importance of considering fire safety and bring importance to the fire extinguisher.
Updates

Reason: I have not received sufficient designs or design that I feel communicates my message on the "green" eco friendliness of this extinguisher versus competitors and importance to have in household.

Target Market(s)

Home owners, renters, parents, eco conscious people, hikers, boat owners since eco

Colors
9bcb3c
eb1f27
acd036
fef8f2
f78f20
f37122
cadf82

Requirements
Must have
• Must have picture of the vornaline extinguisher that was included, must reflect eco friendliness so need green; must look contemporary modern; be bold; exude importance of extinguishers and bring awareness of fire
Nice to have
• I would like to see green; since its very earth friendly its not a bad idea to show how it can be used in earth friendly situations such as on marina and camp but main target is homeowner/renter - for household use
Should not have
• do not include pictures of a traditional fire extinguisher; do not like decorative type fonts; format should be modern; no use of cartoon pictures to reflect fire elements - real pictures.

```html
<!DOCTYPE html>
<html lang="en">
<head>
<meta charset="utf-8">
<title>Vornaline – Eco Fire Extinguisher Postcard</title>
<link href="https://fonts.googleapis.com/css2?family=Roboto+Condensed:wght@400;700;900&display=swap" rel="stylesheet">
<style>
  :root {
    --green: #9bcb3c;
    --green-light: #cadf82;
    --green-deep: #4f7f1c;
    --red: #eb1f27;
    --red-deep: #b0141a;
    --cream: #fef8f2;
    --ink: #161616;
    --white: #ffffff;
  }
  * { margin: 0; padding: 0; box-sizing: border-box; }
  html, body { width: 1200px; height: 390px; overflow: hidden; background: var(--white); }
  body { position: relative; font-family: "Roboto Condensed", "Arial Narrow", sans-serif; }

  .card { position: absolute; top: 5px; width: 580px; height: 378px; overflow: hidden; }
  .card--front { left: 8px; background: radial-gradient(ellipse at 55% 45%, var(--green-light) 0%, var(--green) 45%, var(--green-deep) 100%); }
  .card--back { left: 612px; background: radial-gradient(ellipse at 85% 55%, var(--green-light) 0%, var(--green) 50%, var(--green-deep) 100%); }

  .product-photo { position: absolute; background: linear-gradient(90deg, #7d0d12 0%, var(--red) 40%, #f2545a 55%, var(--red-deep) 100%); border-radius: 40px 40px 0 0; }
  .card--front .product-photo { left: 35px; top: 40px; width: 165px; height: 338px; }

  .brand-tag { position: absolute; background: var(--ink); color: var(--white); font-weight: 900; font-size: 24px; letter-spacing: -0.5px; text-transform: uppercase; display: flex; align-items: center; justify-content: center; }
  .card--front .brand-tag { left: 447px; top: 16px; width: 128px; height: 55px; }
  .card--back .brand-tag { left: 364px; top: 16px; width: 131px; height: 55px; }

  .headline { position: absolute; left: 227px; top: 59px; color: var(--white); font-weight: 700; font-size: 29px; line-height: 31px; text-transform: uppercase; letter-spacing: 0.2px; }
  .claim-bar { position: absolute; left: 227px; top: 176px; width: 182px; height: 19px; background: var(--red); color: var(--white); font-weight: 700; font-size: 12.5px; line-height: 19px; padding-left: 5px; }
  .claim-body { position: absolute; left: 227px; top: 202px; width: 240px; color: var(--white); font-weight: 700; font-size: 10.5px; line-height: 15px; }
  .eco-seal { position: absolute; left: 452px; top: 258px; }

  .back-panel { position: absolute; left: 0; top: 0; width: 366px; height: 378px; background: radial-gradient(ellipse at 50% 40%, #f0555b 0%, var(--red) 50%, var(--red-deep) 100%); }
  .back-panel .product-photo { left: 20px; top: 147px; width: 52px; height: 209px; border-radius: 14px 14px 4px 4px; }
  .fine-print { position: absolute; left: 38px; top: 40px; width: 175px; color: var(--cream); font-size: 4.5px; line-height: 8px; font-weight: 700; }
  .rule-lines { position: absolute; }
  .back-panel .rule-lines { left: 40px; top: 113px; }
  .card--back > .rule-lines { left: 395px; top: 111px; }
  .note { position: absolute; left: 89px; top: 115px; width: 240px; color: var(--cream); font-weight: 700; font-size: 18px; line-height: 19px; text-transform: uppercase; }
  .address-box { position: absolute; left: 395px; top: 276px; width: 166px; height: 73px; background: var(--white); border-radius: 6px; }
</style>
</head>
<body>

<section class="card card--front">
  <div class="product-photo" role="img" aria-label="Photo of the red Vornaline foam fire extinguisher can"></div>
  <div class="brand-tag">Vornaline</div>
  <h1 class="headline">Vornaline –<br>A Revolutionary<br>New Fire Extinguisher</h1>
  <p class="claim-bar">Vornaline is the ONLY 100%</p>
  <p class="claim-body">Bio-Degradable, Non-Toxic, Non-Corrosive Fire Extinguishing Foam that is SafeMark listed and certified by both the Greenleaf Safety Council and the National Woodland Board.</p>
  <svg class="eco-seal" width="120" height="120" viewBox="0 0 120 120" aria-hidden="true">
    <circle cx="60" cy="60" r="54" fill="none" stroke="var(--cream)" stroke-width="3" opacity="0.75"/>
    <circle cx="60" cy="60" r="42" fill="var(--cream)" opacity="0.35"/>
  </svg>
</section>

<section class="card card--back">
  <div class="back-panel">
    <p class="fine-print">Vornaline is the ONLY 100% bio-degradable, non-toxic fire extinguishing foam. SafeMark listed and certified safe for homes, boats and camps. Proudly approved by the National Woodland Board.</p>
    <svg class="rule-lines" width="284" height="214" viewBox="0 0 284 214" aria-hidden="true">
      <g stroke="var(--cream)" stroke-width="1" opacity="0.5">
        <line x1="0" y1="2" x2="284" y2="2"/><line x1="0" y1="21" x2="284" y2="21"/>
        <line x1="0" y1="40" x2="284" y2="40"/><line x1="0" y1="59" x2="284" y2="59"/>
        <line x1="0" y1="78" x2="284" y2="78"/><line x1="0" y1="97" x2="284" y2="97"/>
        <line x1="0" y1="116" x2="284" y2="116"/><line x1="0" y1="135" x2="284" y2="135"/>
        <line x1="0" y1="154" x2="284" y2="154"/><line x1="0" y1="173" x2="284" y2="173"/>
        <line x1="0" y1="192" x2="284" y2="192"/><line x1="0" y1="211" x2="284" y2="211"/>
      </g>
    </svg>
    <div class="product-photo" role="img" aria-label="Photo of the Vornaline extinguisher with product label"></div>
    <p class="note">If you like the designs I can do any change you need it is not a problem, and add your text. Fire pictures and more..</p>
  </div>
  <div class="brand-tag">Vornaline</div>
  <svg class="rule-lines" width="166" height="140" viewBox="0 0 166 140" aria-hidden="true">
    <g stroke="var(--cream)" stroke-width="1" opacity="0.6">
      <line x1="0" y1="2" x2="166" y2="2"/><line x1="0" y1="21" x2="166" y2="21"/>
      <line x1="0" y1="40" x2="166" y2="40"/><line x1="0" y1="59" x2="166" y2="59"/>
      <line x1="0" y1="78" x2="166" y2="78"/><line x1="0" y1="97" x2="166" y2="97"/>
      <line x1="0" y1="116" x2="166" y2="116"/><line x1="0" y1="135" x2="166" y2="135"/>
    </g>
  </svg>
  <div class="address-box"></div>
</section>

</body>
</html>
```